Terraquest NW PPT template - non-profit company - minerals, energy, water, geothermal resources

Terraquest NW requires two (Letter-sized and 16:9)simple, flexible and clean PowerPoint templates that can be used for corporate and research project presentations and meeting materials

Each layout should have correct colours, fonts and size as a default (focus area colours for headings; secondary colours for body text). Each slide should have the Terraquest NW logo. Slide number should be automatically generated, with no slide number on title slide.

Target Market(s)

Varied, but almost always professional: Government; Community leaders; Mineral/Energy industries; and Academic researchers.

Font styles to use
Serif
Sans Serif
Other font styles liked:
• Calibri, or whatever in style guide

Requirements
Must have
• Two version that we can use – both need to match:
- 16:9 slide size for on-screen presentations; and
- Letter (8.5 x 11 inch) for meeting materials that are printed.

Must use colours in logo as listed in the style guide
Nice to have
• Consistency
Should not have
• Should not be black and white - needs colour

```html
<!DOCTYPE html>
<html lang="en">
<head>
<meta charset="utf-8">
<title>Terraquest NW – Presentation Template</title>
<link rel="stylesheet" href="https://fonts.googleapis.com/css2?family=Fira+Sans:wght@400;500;600&family=Source+Sans+3:wght@400;600&display=swap">
<style>
:root{
  --page:#f3eff5;
  --slide:#ffffff;
  --ink:#4a5868;
  --body:#6f7885;
  --muted:#b3b8c0;
  --accent:#f0a04b;
  --minerals:#d9733a;
  --energy:#0aa34a;
  --water:#2aa9c9;
  --comms:#959aa4;
  --map:#fbf8dc;
}
*{box-sizing:border-box;margin:0;padding:0}
html,body{width:1200px;height:2266px;overflow:hidden;background:var(--page)}
body{position:relative;font-family:"Source Sans 3",Arial,sans-serif;color:var(--ink)}
.slide{position:absolute;width:562px;height:317px;background:var(--slide);overflow:hidden;box-shadow:0 4px 14px rgba(80,70,100,.12)}
.col-l{left:33px}.col-r{left:604px}
.r1{top:38px}.r2{top:394px}.r3{top:751px}.r4{top:1109px}.r5{top:1466px}.r6{top:1823px}
.tint{background:linear-gradient(135deg,#f7f4fa,#fff 55%)}
.photo{position:absolute}
.ph-snow{background:linear-gradient(180deg,#e9eaee 0%,#dcdfe4 50%,#9aa3a2 75%,#56625c 100%)}
.ph-lake{background:linear-gradient(180deg,#bfe0e6 0%,#8fb8bd 35%,#4f7268 55%,#3c8a93 75%,#2e5a5e 100%)}
.ph-field{background:linear-gradient(180deg,#5f7a2c 0%,#7a8f35 40%,#c9c2b0 45%,#c9c2b0 52%,#6f8a2e 58%,#4f6a20 100%)}
.ph-falls{background:linear-gradient(160deg,#5e7a3c 0%,#3f5f4a 35%,#d7e3e2 50%,#2f6a66 65%,#1f4b4a 100%)}
.title{position:absolute;font-family:"Fira Sans",Arial,sans-serif;font-weight:500;font-size:15px;line-height:14px;color:var(--ink);padding-left:12px;border-left:2px solid var(--accent)}
.brand{position:absolute;font-family:"Fira Sans",Arial,sans-serif;font-weight:500;color:var(--ink);display:flex;align-items:center;gap:4px;white-space:nowrap}
.brand::before{content:"";width:.55em;height:.55em;border-radius:50%;background:var(--minerals)}
.brand.sm{font-size:9px;top:36px;right:36px}
.copy{position:absolute;font-size:5.4px;line-height:8.6px;color:var(--body)}
.copy p+p{margin-top:4px}
.rail{position:absolute;right:10px;top:0;bottom:0;width:16px;border-left:1px solid #ececf0}
.rail span{position:absolute;left:4px;top:50%;transform:translate(-50%,-50%) rotate(-90deg);transform-origin:center;white-space:nowrap;font-size:4.4px;letter-spacing:1px;color:var(--muted);margin-left:8px}
.pageno{position:absolute;right:12px;bottom:14px;font-size:5.5px;font-weight:600;letter-spacing:1px;color:var(--ink)}
.section .brand{font-size:15px;left:40px;top:58px}
.section .corner{position:absolute;left:0;top:0;width:63px;height:63px;clip-path:polygon(0 0,100% 0,0 100%)}
.section .band{position:absolute;inset:0;clip-path:polygon(562px 40px,562px 317px,245px 317px)}
.section .ring{position:absolute;left:360px;top:120px;width:228px;height:228px;border-radius:50%;background:#f4f4f6;box-shadow:0 0 20px rgba(0,0,0,.08)}
.section .disc{position:absolute;left:383px;top:143px;width:182px;height:182px;border-radius:50%;background:#fff;display:flex;align-items:center;justify-content:center;padding-right:0}
.section .heading{position:absolute;left:40px;top:140px;height:76px;padding-left:13px;border-left:2px solid}
.section .kicker{font-size:8px;letter-spacing:2.6px;color:var(--comms);margin-top:14px}
.section h2{font-family:"Fira Sans",Arial,sans-serif;font-weight:500;font-size:26px;color:var(--ink);margin-top:1px}
.minerals .corner,.minerals .band{background:var(--minerals)}.minerals .heading{border-color:var(--minerals)}
.energy .corner,.energy .band{background:var(--energy)}.energy .heading{border-color:var(--energy)}
.water .corner,.water .band{background:var(--water)}.water .heading{border-color:var(--water)}
.comms .corner,.comms .band{background:var(--comms)}.comms .heading{border-color:var(--comms)}
.section svg{fill:none;stroke-width:2.6;stroke-linecap:round;stroke-linejoin:round}
.titlebox{position:absolute;background:#fff}
.byline{font-size:5.6px;letter-spacing:2px;color:var(--muted);margin-top:3px;font-family:"Source Sans 3",Arial,sans-serif;font-weight:400}
.contact{position:absolute;left:35px;font-size:6.6px;color:var(--ink);display:flex;gap:8px;align-items:flex-start;line-height:9px}
.contact svg{flex:none}
</style>
</head>
<body>

<!-- Title slide -->
<section class="slide col-l r1 tint">
  <div class="photo ph-snow" style="left:0;top:120px;width:562px;height:197px" role="img" aria-label="Photo of snowy mountain peaks above a misty forest"></div>
  <div class="brand" style="left:37px;top:88px;font-size:18px">Terraquest NW</div>
  <div class="titlebox" style="left:0;top:186px;width:264px;height:70px">
    <div class="title" style="left:22px;top:12px;height:50px;font-size:14px;line-height:13px;padding-top:5px">Place for the<br>Presentation title<div class="byline">MAYA ELLISON / 21.01.2020</div></div>
  </div>
</section>

<!-- Text slide -->
<section class="slide col-r r1 tint">
  <div class="title" style="left:22px;top:20px;height:40px;padding-top:5px">Place for the<br>Slide Title</div>
  <div class="brand sm" style="top:42px">Terraquest NW</div>
  <div class="copy" style="left:25px;top:74px;width:494px">
    <p>Our teams gather public geoscience data across the region to support sound decisions on land, water and resources. Each project is shaped with communities, industry partners and academic researchers, and every result is shared openly so that local groups and agencies can plan with confidence. Field programs run through the summer season and reports follow.</p>
    <p>Mapping work this year focused on groundwater basins in the interior, with new wells logged and sampled. Results show stable levels in most areas, with a few sites needing further study. Data sets are now online and free to use for planning, teaching and research.</p>
    <p>Energy studies looked at heat flow in deep rock and the potential for local geothermal power. Early models point to several promising zones near existing towns. Partners will drill test holes next spring to confirm the readings and measure temperature at depth before any plans move ahead.</p>
    <p>Mineral surveys covered a wide belt in the north using airborne tools and ground checks. New maps reveal trends that may guide future exploration while protecting sensitive land and water.</p>
    <p>Next steps include community sessions, updated reports and a shared data portal for all partners and the public.</p>
  </div>
  <div class="rail"><span>STRICTLY CONFIDENTIAL · NOT FOR PUBLIC DISTRIBUTION</span></div>
  <div class="pageno">05</div>
</section>

<!-- Text + image slide -->
<section class="slide col-l r2 tint">
  <div class="title" style="left:22px;top:68px;height:40px;padding-top:5px">Place for the<br>Slide Title</div>
  <div class="brand sm">Terraquest NW</div>
  <div class="copy" style="left:25px;top:125px;width:205px">
    <p>Our teams gather public geoscience data across the region to support sound decisions on land, water and resources. Each project is shaped with communities, industry partners and researchers, and results are shared openly so that local groups can plan with confidence. Field programs run through the summer and reports follow in the autumn. New maps and data sets are free to use for planning, teaching and research across the province.</p>
  </div>
  <div class="photo ph-lake" style="left:274px;top:83px;width:249px;height:166px" role="img" aria-label="Photo of a mountain lake reflecting rocky peaks"></div>
  <div class="rail"><span>STRICTLY CONFIDENTIAL · NOT FOR PUBLIC DISTRIBUTION</span></div>
  <div class="pageno">05</div>
</section>

<!-- Image left slide -->
<section class="slide col-r r2">
  <div class="photo ph-field" style="left:0;top:0;width:253px;height:317px" role="img" aria-label="Aerial photo of a road crossing green fields"></div>
  <div class="brand sm">Terraquest NW</div>
  <div class="title" style="left:277px;top:82px;height:40px;padding-top:5px">Place for the<br>Slide Title</div>
  <div class="copy" style="left:280px;top:136px;width:240px">
    <p>Our teams gather public geoscience data across the region to support sound decisions on land, water and resources. Each project is shaped with communities, industry partners and researchers, and results are shared openly so local groups can plan with confidence. Field programs run through the summer and reports follow in the autumn. New maps are free to use.</p>
  </div>
  <div class="rail"><span>STRICTLY CONFIDENTIAL · NOT FOR PUBLIC DISTRIBUTION</span></div>
  <div class="pageno">05</div>
</section>

<!-- Image centre slide -->
<section class="slide col-l r3 tint">
  <div class="title" style="left:22px;top:146px;height:40px;padding-top:5px">Place for the<br>Slide Title</div>
  <div class="photo ph-falls" style="left:182px;top:0;width:199px;height:317px" role="img" aria-label="Aerial photo of a waterfall beside a forested park"></div>
  <div class="brand sm">Terraquest NW</div>
  <div class="copy" style="left:404px;top:112px;width:106px">
    <p>Our teams gather public geoscience data across the region to support sound decisions on land and water. Each project is shaped with communities and partners, and results are shared openly so local groups can plan with care.</p>
  </div>
  <div class="rail"><span>STRICTLY CONFIDENTIAL · NOT FOR PUBLIC DISTRIBUTION</span></div>
  <div class="pageno">05</div>
</section>

<!-- Full image slide -->
<section class="slide col-r r3">
  <div class="photo ph-lake" style="left:0;top:0;width:541px;height:317px" role="img" aria-label="Photo of a turquoise mountain lake with forested slopes"></div>
  <div class="titlebox" style="left:0;top:12px;width:207px;height:60px">
    <div class="title" style="left:22px;top:12px;height:40px;padding-top:5px">Place for the<br>Slide Title</div>
  </div>
  <div class="rail"><span>STRICTLY CONFIDENTIAL · NOT FOR PUBLIC DISTRIBUTION</span></div>
  <div class="pageno">05</div>
</section>

<!-- Section breaks -->
<section class="slide col-l r4 section minerals tint">
  <div class="corner"></div><div class="band"></div>
  <div class="brand">Terraquest NW</div>
  <div class="heading"><div class="kicker">P4. MINERALS</div><h2>Section Break</h2></div>
  <div class="ring"></div>
  <div class="disc">
    <svg width="100" height="100" viewBox="0 0 100 100" stroke="var(--minerals)">
      <path d="M12 62 C22 30 48 14 84 14 C62 22 40 38 24 66 Z"/>
      <path d="M46 38 L88 84 L82 90 L40 44"/>
    </svg>
  </div>
</section>

<section class="slide col-r r4 section energy tint">
  <div class="corner"></div><div class="band"></div>
  <div class="brand">Terraquest NW</div>
  <div class="heading"><div class="kicker">P4. ENERGY</div><h2>Section Break</h2></div>
  <div class="ring"></div>
  <div class="disc">
    <svg width="96" height="100" viewBox="0 0 96 100" stroke="var(--energy)">
      <path d="M48 24 C30 24 22 38 24 50 C26 60 34 64 36 72 L60 72 C62 64 70 60 72 50 C74 38 66 24 48 24 Z"/>
      <path d="M38 78 H58 M40 84 H56 M44 90 H52"/>
      <path d="M48 6 V14 M20 16 L26 22 M76 16 L70 22 M8 44 H16 M80 44 H88 M14 70 L20 66 M82 70 L76 66"/>
    </svg>
  </div>
</section>

<section class="slide col-l r5 section water tint">
  <div class="corner"></div><div class="band"></div>
  <div class="brand">Terraquest NW</div>
  <div class="heading"><div class="kicker">P4. WATER</div><h2>Section Break</h2></div>
  <div class="ring"></div>
  <div class="disc">
    <svg width="80" height="110" viewBox="0 0 80 110" stroke="var(--water)">
      <path d="M40 6 C30 30 6 54 6 74 C6 94 22 106 40 106 C58 106 74 94 74 74 C74 54 50 30 40 6 Z"/>
      <path d="M18 76 C18 86 24 92 30 94"/>
    </svg>
  </div>
</section>

<section class="slide col-r r5 section comms tint">
  <div class="corner"></div><div class="band"></div>
  <div class="brand">Terraquest NW</div>
  <div class="heading"><div class="kicker">P4. COMUNICATIONS</div><h2>Section Break</h2></div>
  <div class="ring"></div>
  <div class="disc">
    <svg width="90" height="90" viewBox="0 0 90 90" stroke="var(--comms)" stroke-width="2.2">
      <path d="M30 6 H60 A10 10 0 0 1 70 16 V26 A10 10 0 0 1 60 36 H40 L32 44 V36 H30 A10 10 0 0 1 20 26 V16 A10 10 0 0 1 30 6 Z"/>
      <circle cx="36" cy="21" r="1"/><circle cx="45" cy="21" r="1"/><circle cx="54" cy="21" r="1"/>
      <circle cx="45" cy="52" r="7"/><path d="M31 80 V74 A14 14 0 0 1 59 74 V80 Z"/>
      <circle cx="20" cy="58" r="6"/><path d="M6 84 V78 A13 13 0 0 1 28 70"/>
      <circle cx="70" cy="58" r="6"/><path d="M84 84 V78 A13 13 0 0 0 62 70"/>
      <path d="M6 84 H31 M59 84 H84"/>
    </svg>
  </div>
</section>

<!-- Map slide -->
<section class="slide col-l r6">
  <div style="position:absolute;left:0;top:0;width:35px;height:317px;border-right:1px solid #ececf0">
    <div class="title" style="left:17px;top:158px;transform:translate(-50%,-50%) rotate(-90deg);white-space:nowrap;border:none;padding:0;font-size:12px">Place for the Slide Title</div>
  </div>
  <div class="photo" style="left:35px;top:0;width:405px;height:317px;background:var(--map)" role="img" aria-label="Regional map showing districts and rivers"></div>
  <div class="photo" style="left:336px;top:0;width:104px;height:122px;background:#fff;border:1px solid #555" role="img" aria-label="Inset locator map with the region highlighted"></div>
  <div class="brand sm">Terraquest NW</div>
  <div class="copy" style="left:454px;top:112px;width:80px">
    <p>Our teams gather public geoscience data across the region to support sound decisions on land and water. Each project is shaped with communities and partners, and results are shared openly.</p>
  </div>
  <div class="rail"><span>STRICTLY CONFIDENTIAL · NOT FOR PUBLIC DISTRIBUTION</span></div>
  <div class="pageno">05</div>
</section>

<!-- Closing slide -->
<section class="slide col-r r6 tint">
  <div class="photo ph-snow" style="left:0;top:120px;width:562px;height:197px" role="img" aria-label="Photo of snowy mountains above a misty forest"></div>
  <div class="brand" style="left:50px;top:160px;font-size:23px">Terraquest NW</div>
  <div class="titlebox" style="left:265px;top:67px;width:297px;height:164px">
    <div class="title" style="left:35px;top:14px;height:40px;padding-top:7px">Thank You<div class="byline">FOR YOUR TIME</div></div>
    <div style="position:absolute;left:35px;top:70px;font-size:7px;letter-spacing:.4px;color:var(--ink)">PRESENTED BY: MAYA ELLISON</div>
    <div class="contact" style="top:96px">
      <svg width="10" height="10" viewBox="0 0 10 10"><circle cx="5" cy="5" r="5" fill="var(--accent)"/><path d="M1 5 H9 M5 0.5 C2.5 3 2.5 7 5 9.5 M5 0.5 C7.5 3 7.5 7 5 9.5" stroke="#fff" stroke-width=".8" fill="none"/></svg>
      <span>http://www.terraquestnw.org</span>
    </div>
    <div class="contact" style="top:116px">
      <svg width="10" height="13" viewBox="0 0 10 13"><path d="M5 0 C2 0 0 2.2 0 5 C0 8.5 5 13 5 13 C5 13 10 8.5 10 5 C10 2.2 8 0 5 0 Z" fill="var(--accent)"/><circle cx="5" cy="5" r="1.8" fill="#fff"/></svg>
      <span>Terraquest NW, Suite 420 – 88 Harbour Ridge Rd.,<br>Cedar Falls, British Columbia, V0X 1A0, Canada</span>
    </div>
  </div>
</section>

</body>
</html>
```